Company director needs a business card design

I am a semi-retired former senior finance executive who sits on a number of public and private company boards and do some consulting work. I work largely with emerging businesses but deal regularly with top end of town lawyers, bankers etc. I need a thoughtful but relatively conservative design which would also resonate with my younger client base. Some colour would be good. Information limited to name, address, office tel, mobile and email.

Industry/Entity Type

Finance

```html
<!DOCTYPE html>
<html lang="en">
<head>
<meta charset="UTF-8">
<title>Business Card</title>
<link rel="stylesheet" href="https://fonts.googleapis.com/css2?family=Josefin+Sans:wght@700&family=Sarabun:wght@400&family=Open+Sans:wght@400&display=swap">
<style>
  :root {
    --page-bg: #ffffff;
    --card-bg: #cccaca;
    --accent-band: #9a8474;
    --ink: #111111;
    --shadow: rgba(0, 0, 0, 0.35);
  }
  html, body {
    margin: 0;
    padding: 0;
    width: 1200px;
    height: 1000px;
    overflow: hidden;
    background: var(--page-bg);
  }
  .canvas {
    position: relative;
    width: 1200px;
    height: 1000px;
  }
  .card-shadow {
    position: absolute;
    left: 20px;
    top: 690px;
    width: 920px;
    height: 22px;
    border-radius: 50%;
    background: radial-gradient(ellipse at center, var(--shadow) 0%, rgba(0,0,0,0.12) 55%, rgba(0,0,0,0) 75%);
  }
  .card {
    position: absolute;
    left: 48px;
    top: 184px;
    width: 860px;
    height: 516px;
    background: var(--card-bg);
    overflow: hidden;
  }
  .card-bands {
    position: absolute;
    left: 0;
    top: 0;
  }
  .name-plate {
    position: absolute;
    left: 220px;
    top: 260px;
    width: 307px;
    height: 50px;
    background: var(--card-bg);
  }
  .name {
    position: absolute;
    left: 226px;
    top: 271px;
    width: 292px;
    margin: 0;
    font-family: "Josefin Sans", "Century Gothic", sans-serif;
    font-weight: 700;
    font-size: 46px;
    line-height: 1;
    letter-spacing: -1.5px;
    word-spacing: -4px;
    white-space: nowrap;
  }
  .name-first { color: var(--ink); }
  .name-last { color: var(--accent-band); }
  .contact {
    position: absolute;
    display: flex;
    align-items: center;
    color: var(--ink);
    font-family: "Sarabun", sans-serif;
    font-size: 20px;
    letter-spacing: 0.4px;
    line-height: 1;
    white-space: nowrap;
  }
  .contact svg { margin-right: 10px; fill: var(--ink); }
  .contact-address { left: 20px; top: 426px; }
  .contact-region { left: 370px; top: 432px; }
  .contact-mobile { left: 24px; top: 470px; }
  .contact-office { left: 224px; top: 470px; }
  .contact-email { left: 404px; top: 470px; font-family: "Open Sans", sans-serif; font-size: 21px; letter-spacing: 0; }
</style>
</head>
<body>
<div class="canvas">
  <div class="card-shadow"></div>
  <section class="card" aria-label="Business card">
    <svg class="card-bands" width="860" height="516" viewBox="0 0 860 516" aria-hidden="true">
      <polygon fill="var(--accent-band)" points="0,0 266,264 860,264 860,310 218,310 0,98"/>
    </svg>
    <div class="name-plate"></div>
    <h1 class="name"><span class="name-first">YOUR</span> <span class="name-last">NAME</span></h1>

    <div class="contact contact-address">
      <svg width="24" height="22" viewBox="0 0 24 22" aria-hidden="true">
        <path d="M12 1 L1 11 L4 11 L4 21 L10 21 L10 14 L14 14 L14 21 L20 21 L20 11 L23 11 Z"/>
      </svg>
      <span>123 Abandoned Castle Highway</span>
    </div>
    <div class="contact contact-region"><span>Neverland</span></div>

    <div class="contact contact-mobile">
      <svg width="14" height="24" viewBox="0 0 14 24" aria-hidden="true">
        <path d="M2 0 H12 A2 2 0 0 1 14 2 V22 A2 2 0 0 1 12 24 H2 A2 2 0 0 1 0 22 V2 A2 2 0 0 1 2 0 Z M2 3 V18 H12 V3 Z M7 19.5 A1.3 1.3 0 1 0 7 22.1 A1.3 1.3 0 1 0 7 19.5 Z"/>
      </svg>
      <span>01234567890</span>
    </div>

    <div class="contact contact-office">
      <svg width="16" height="24" viewBox="0 0 16 24" aria-hidden="true">
        <path d="M4 0 L7 5 L5 8 C5 12 7 16 9 17 L12 15 L16 20 L13 23 C6 24 0 12 1 3 Z"/>
      </svg>
      <span>222 333 444</span>
    </div>

    <div class="contact contact-email">
      <svg width="26" height="18" viewBox="0 0 26 18" aria-hidden="true">
        <path d="M0 0 H26 V18 H0 Z M3 3 L13 11 L23 3 Z M2 5 V16 L9 10 Z M24 5 L17 10 L24 16 Z M11 12 L4 16 H22 L15 12 L13 13.5 Z" fill-rule="evenodd"/>
      </svg>
      <span>name@company.com</span>
    </div>
  </section>
</div>
</body>
</html>
```